Cedar Basin CBD Apothecary needs label for CBD capsule bottles

I need a 1 1/2"H x 3.5" W label for a cobalt blue glass pill bottle. Looking for apothecary look, but not over the top. I would like a yellow background (ccff00), or combination thereof, and my company logo/name, in addition to the text "PURE CBD CRYSTAL ISOLATE", Dietary Supplement, Ingredients: 99.1% Cannabidiol Crystal Isolate, Lab Tested, ZERO THC, NO FILLERS, Keep Out of Reach of Children, Serving Suggestion: Take one PlantaShell Daily, increase dosage as needed, Storage- cool dry place away from light and heat, www.cbcbdshop.com

Target Market(s)

Adults with health issues, all ages.

Industry/Entity Type

Health And Wellness

Font styles to use
Other font styles liked:
• similar to Algerian. Apothecary fonts.

Colors
fbee3d

Requirements
Must have
• Logo and Company name, "CEDAR BASIN CBD APOTHECARY"
• Yellow to contrast cobalt blue bottles
Nice to have
• Made in Joshua Tree, CA.
• Vegan Capsules
• NO GMO
Should not have
• no pot leaves or anything overtly cannabis related. No script fonts.

```html
<!DOCTYPE html>
<html lang="en">
<head>
<meta charset="utf-8">
<title>Cedar Basin CBD Apothecary – Capsule Label</title>
<link href="https://fonts.googleapis.com/css2?family=Oswald:wght@500;700&display=swap" rel="stylesheet">
<style>
  :root {
    --canvas-bg: #a6b81f;
    --label-top: #c9e04a;
    --label-mid: #d6e86a;
    --label-glow: #8fcf52;
    --tan: #9c9a62;
    --purple: #5a1f56;
    --purple-deep: #3f1240;
    --ink: #5b1a55;
    --frame: #ffffff;
    --badge-dark: #3a3a32;
    --badge-green: #8fbf6a;
  }
  html, body {
    margin: 0;
    padding: 0;
    width: 1200px;
    height: 1200px;
    overflow: hidden;
    background: var(--canvas-bg);
  }
  .canvas {
    position: relative;
    width: 1200px;
    height: 1200px;
  }
  .label {
    position: absolute;
    left: 220px;
    top: 120px;
    width: 760px;
    height: 960px;
    overflow: hidden;
    background:
      radial-gradient(ellipse 60% 22% at 50% 4%, var(--label-glow), transparent 70%),
      linear-gradient(180deg, var(--label-top) 0%, var(--label-mid) 55%, var(--label-top) 100%);
  }
  .label-art {
    position: absolute;
    inset: 0;
  }
  .brand {
    position: absolute;
    top: 170px;
    left: 0;
    width: 100%;
    display: flex;
    align-items: center;
    justify-content: center;
    gap: 14px;
  }
  .brand-dot {
    width: 22px;
    height: 22px;
    border-radius: 50%;
    background: var(--ink);
  }
  .brand-name {
    font-family: "Oswald", sans-serif;
    font-weight: 700;
    font-size: 30px;
    letter-spacing: 2px;
    color: var(--ink);
    margin: 0;
  }
  .product-title {
    position: absolute;
    top: 330px;
    left: 0;
    width: 100%;
    margin: 0;
    text-align: center;
    font-family: "Oswald", sans-serif;
    font-weight: 700;
    font-size: 56px;
    line-height: 74px;
    color: var(--ink);
    letter-spacing: 0.5px;
  }
  .origin-tag {
    position: absolute;
    top: 646px;
    left: 222px;
    width: 316px;
    height: 40px;
    background: var(--purple);
    color: var(--label-top);
    font-family: "Oswald", sans-serif;
    font-weight: 700;
    font-size: 20px;
    line-height: 40px;
    text-align: center;
    letter-spacing: 0.5px;
  }
</style>
</head>
<body>
  <main class="canvas">
    <section class="label">
      <svg class="label-art" viewBox="0 0 760 960" width="760" height="960" aria-hidden="true">
        <polygon class="band-tan" points="0,575 380,765 760,575 760,960 0,960" fill="var(--tan)"/>
        <polygon class="band-purple" points="0,735 380,905 760,735 760,960 0,960" fill="var(--purple)"/>
        <polygon class="band-purple-deep" points="230,960 380,885 530,960" fill="var(--purple-deep)"/>
        <g class="sketch-frame" fill="none" stroke="var(--frame)" stroke-width="3" opacity="0.85">
          <rect x="40" y="36" width="680" height="888"/>
          <rect x="52" y="48" width="656" height="864"/>
          <rect x="64" y="58" width="634" height="846"/>
          <rect x="76" y="70" width="610" height="822" stroke-width="2"/>
        </g>
        <circle class="badge-vegan" cx="160" cy="780" r="46" fill="var(--badge-dark)"/>
        <circle class="badge-nongmo" cx="600" cy="780" r="46" fill="var(--badge-green)"/>
      </svg>

      <div class="brand">
        <span class="brand-dot"></span>
        <p class="brand-name">CEDAR BASIN CBD APOTHECARY</p>
      </div>

      <h1 class="product-title">PURE<br>CBD<br>CRYSTAL<br>ISOLATE</h1>

      <div class="origin-tag">MADE IN JOSHUA TREE, CA.</div>
    </section>
  </main>
</body>
</html>
```